Business Card Design

I need a business card design for a photography business that specializes in headshots and portraits.

Target Market(s)

Business professionals, actors, actresses

Industry/Entity Type

Business

Contact Information for Business Card

Cobalt Ridge Photography, Greg Whitlow, 5817 Kellerman Ave, Suite 416, Fort Wayne, IN 46915, 260.555.0187, www.cobaltridgephoto.example. greg.whitlow@cobaltridgephoto.example

Requirements
Must have
• The business card should state the type of photography services offered: headshots and portraits.

```html
<!DOCTYPE html>
<html lang="en">
<head>
<meta charset="utf-8">
<title>Cobalt Ridge Photography – Business Card</title>
<link rel="stylesheet" href="https://fonts.googleapis.com/css2?family=Questrial&display=swap">
<style>
  :root {
    --card-bg: #000000;
    --ink-white: #ffffff;
    --ink-orange: #f39a2e;
    --ink-grey: #9b9b9b;
    --rule-grey: #3a3a3a;
  }
  * { margin: 0; padding: 0; box-sizing: border-box; }
  html, body {
    width: 1200px;
    height: 705px;
    overflow: hidden;
    background: var(--card-bg);
  }
  .card {
    position: relative;
    width: 1200px;
    height: 705px;
    background: var(--card-bg);
    font-family: "Questrial", "Century Gothic", sans-serif;
    color: var(--ink-white);
  }
  .studio-name {
    position: absolute;
    top: 42px;
    left: 0;
    width: 100%;
    text-align: center;
    font-size: 62px;
    font-weight: 400;
    letter-spacing: 0.5px;
    line-height: 1;
  }
  .studio-name .accent { color: var(--ink-orange); }

  .brand-mark {
    position: absolute;
    left: 300px;
    top: 290px;
    display: flex;
    align-items: center;
    gap: 34px;
  }
  .brand-mark .ring {
    width: 120px;
    height: 120px;
    flex: none;
  }
  .brand-text { display: flex; flex-direction: column; align-items: flex-end; }
  .photographer-name {
    font-size: 66px;
    color: var(--ink-orange);
    line-height: 1;
  }
  .services {
    margin-top: 14px;
    font-size: 22px;
    letter-spacing: 2px;
    color: var(--ink-grey);
    line-height: 1;
  }

  .address {
    position: absolute;
    top: 570px;
    left: 0;
    width: 100%;
    text-align: center;
    font-size: 28px;
    line-height: 1;
  }
  .rule {
    position: absolute;
    top: 614px;
    left: 40px;
    right: 40px;
    height: 1px;
    background: var(--rule-grey);
  }
  .contact-row {
    position: absolute;
    top: 628px;
    left: 40px;
    right: 40px;
    display: flex;
    justify-content: space-between;
    font-size: 24px;
    line-height: 1;
  }
  .contact-row .web { color: var(--ink-orange); }
</style>
</head>
<body>
  <div class="card">
    <h1 class="studio-name">Cobalt Ridge <span class="accent">Photography</span></h1>

    <div class="brand-mark">
      <svg class="ring" viewBox="0 0 120 120" aria-hidden="true">
        <circle cx="60" cy="60" r="55" fill="none" stroke="#f39a2e" stroke-width="5"/>
      </svg>
      <div class="brand-text">
        <p class="photographer-name">Greg Whitlow</p>
        <p class="services">HEADSHOTS &amp; PORTRAITS</p>
      </div>
    </div>

    <p class="address">5817 Kellerman Ave, Suite 416, Fort Wayne, IN 46915</p>
    <div class="rule"></div>
    <div class="contact-row">
      <span class="phone">260.555.0187</span>
      <span class="web">www.cobaltridgephoto.example</span>
      <span class="email">greg.whitlow@cobaltridgephoto.example</span>
    </div>
  </div>
</body>
</html>
```